Business Card Design Project

A double sided business card for presentation to business leaders in corporate.

Target Market(s)

Corporate, business professionals, HR

Industry/Entity Type

Business

Requirements
Must have
• FRONT

Logo

www.brightfernco.com.au

BACK

Maren Tollvey-Hart
Director

+ 61 (0) 418 556 230
maren@brightfernco.com.au
www.brightfernco.com.au

brightfern through energy and employee engagement

("ripples" of logo, bottom corner)

Must be:
- double sided
size: 86 x 54mm
supplied as one pdf with crop marks shown (+- 1mm, with 2-3 mm bleed)

```html
<!DOCTYPE html>
<html lang="en">
<head>
<meta charset="utf-8">
<title>Brightfern Co — Business Card Set</title>
<link rel="stylesheet" href="https://fonts.googleapis.com/css2?family=Questrial&display=swap">
<style>
  :root {
    --backdrop: #e9e5e0;
    --label: #1e1e1e;
    --paper: #ffffff;
    --plum: #7a2a68;
    --plum-light: #8e3c7d;
    --plum-dark: #691e5a;
    --charcoal: #4a4a4c;
    --ink: #444446;
    --white: #ffffff;
  }
  * { box-sizing: border-box; margin: 0; padding: 0; }
  html, body {
    width: 1200px; height: 788px; overflow: hidden;
    background: var(--backdrop);
    font-family: "Questrial", "Century Gothic", sans-serif;
  }
  .sheet { position: relative; width: 1200px; height: 788px; }

  .card-label {
    position: absolute; width: 508px; text-align: center;
    font-family: Arial, Helvetica, sans-serif; font-size: 20px; color: var(--label);
  }
  .card {
    position: absolute; width: 508px; height: 318px;
    border-radius: 22px; overflow: hidden;
    box-shadow: 0 4px 10px rgba(0,0,0,0.18);
  }
  .card--front { left: 70px; top: 50px; background: var(--paper); }
  .card--back-light { left: 640px; top: 50px; background: var(--paper); }
  .card--back-grey { left: 70px; top: 437px; background: var(--charcoal); }
  .card--back-plum { left: 640px; top: 437px;
    background: linear-gradient(90deg, var(--plum-light), var(--plum-dark)); }

  .card-shapes { position: absolute; inset: 0; width: 508px; height: 318px; }

  .brand-name { position: absolute; white-space: nowrap; line-height: 1; letter-spacing: -0.5px; }

  .front-name { left: 38px; top: 100px; font-size: 46px; color: var(--plum); }

  .contact-name { position: absolute; left: 38px; top: 200px; font-size: 16px; color: var(--ink); }
  .contact-name .role { font-size: 13px; }
  .contact-phone { position: absolute; left: 38px; top: 227px; font-size: 13.5px; color: var(--ink); }
  .contact-strip {
    position: absolute; left: 20px; right: 14px; top: 282px;
    font-size: 13px; color: var(--white); white-space: nowrap;
  }
  .contact-strip .divider { margin: 0 8px; }

  .centre-name { left: 0; right: 0; top: 125px; text-align: center; font-size: 64px; }
  .card--back-light .centre-name { color: var(--plum); }
  .card--back-plum .centre-name { color: var(--white); }

  .spaced-web {
    position: absolute; left: 0; right: 0; top: 276px; text-align: center;
    font-size: 13px; letter-spacing: 4px;
  }
  .card--back-light .spaced-web { color: var(--ink); }
  .card--back-plum .spaced-web { color: var(--white); }

  .grey-name { left: 30px; top: 90px; font-size: 64px; color: var(--white); }
  .grey-web { position: absolute; left: 28px; top: 285px; font-size: 13px; color: var(--white); }
</style>
</head>
<body>
<main class="sheet">

  <div class="card-label" style="left:70px; top:20px;">Front</div>
  <div class="card-label" style="left:640px; top:20px;">Back - 1</div>
  <div class="card-label" style="left:70px; top:406px;">Back - 2</div>
  <div class="card-label" style="left:640px; top:406px;">Back - 3</div>

  <section class="card card--front">
    <svg class="card-shapes" viewBox="0 0 508 318" aria-hidden="true">
      <defs>
        <linearGradient id="plumBand" x1="0" x2="1" y1="0" y2="0">
          <stop offset="0" stop-color="#8e3c7d"/>
          <stop offset="1" stop-color="#691e5a"/>
        </linearGradient>
      </defs>
      <path d="M440,0 L508,0 L508,112 C470,170 400,225 305,250 C400,205 455,120 440,0 Z" fill="#4a4a4c"/>
      <path d="M0,265 C170,262 300,250 390,222 C440,202 480,160 508,128 L508,318 L0,318 Z" fill="url(#plumBand)"/>
    </svg>
    <p class="brand-name front-name">brightfern co</p>
    <p class="contact-name">Maren Tollvey-Hart, <span class="role">Director</span></p>
    <p class="contact-phone">phone : + 61 (0) 418 556 230</p>
    <p class="contact-strip">email : maren@brightfernco.com.au<span class="divider">|</span>web : www.brightfernco.com.au</p>
  </section>

  <section class="card card--back-light">
    <p class="brand-name centre-name">brightfern co</p>
    <p class="spaced-web">www.brightfernco.com.au</p>
  </section>

  <section class="card card--back-grey">
    <p class="brand-name grey-name">brightfern</p>
    <p class="grey-web">www.brightfernco.com.au</p>
  </section>

  <section class="card card--back-plum">
    <p class="brand-name centre-name">brightfern co</p>
    <p class="spaced-web">www.brightfernco.com.au</p>
  </section>

</main>
</body>
</html>
```